"Landing Page Design for Premium Eco-Friendly Laundry Strips – Plooifris.nl"

We need a visually appealing and high-converting landing page for our premium laundry strips, emphasizing luxury, sustainability, and ease of use. The page should include sections such as:

Hero Section: A compelling introduction with a strong headline, subheadline, and a clear call-to-action (CTA).
Product Benefits: Highlighting key features like eco-friendliness, long-lasting scent, and hypoallergenic qualities.
Product Description: Focusing on innovation and sustainability.
How It Works: Simple, visual steps for using the product.
Customer Reviews: Authentic testimonials to build trust and social proof.
FAQ Section: Addressing common concerns about the product.
The design should maintain a luxurious aesthetic while ensuring clarity and user-friendliness. We also offer free shipping on all orders, a key differentiator to be prominently displayed. All texts and translations are already provided for implementation. Please deliver the design in Figma format."

Target Market(s)

"Eco-conscious consumers and families seeking premium and sustainable laundry solutions. Target age group: 25-50, predominantly women who prioritize luxury and environmental impact."

Industry/Entity Type

"Laundry care and eco-friendly consumer goods."

Coding

Requirements
Must have
• A visually luxurious design emphasizing premium quality and eco-friendliness. Clear call-to-actions (e.g., 'Try Now – Free Shipping'). Sections for product benefits, how it works, customer reviews, and FAQ. Highlight free shipping with no minimum order prominently."
Nice to have
• Elegant, minimalist animations to enhance the premium feel. Subtle use of gold and black to emphasize luxury, with a touch of green for sustainability. Interactive customer reviews section (e.g., carousel or testimonials)."
Should not have
• Overly cluttered designs or overwhelming text blocks. Generic stock photos not aligned with our brand identity. Bright or overly playful color schemes that detract from the premium feel."

```html
<!DOCTYPE html>
<html lang="en">
<head>
<meta charset="utf-8">
<title>Plooifris.nl – Premium Laundry Strips</title>
<link href="https://fonts.googleapis.com/css2?family=Inter:wght@400;500;600;700&family=Jost:wght@500;600&display=swap" rel="stylesheet">
<style>
:root{
  --gold:#e2ad2b;
  --gold-light:#f0cf4a;
  --yellow:#efcf48;
  --black:#0d0d0d;
  --ink:#1d1d1d;
  --slate:#29303d;
  --slate-dark:#2b323f;
  --beige:#f1ebe1;
  --cream:#f6efc8;
  --grey-bg:#f7f7f7;
  --muted:#777;
  --line:#ececec;
  --white:#fff;
}
*{margin:0;padding:0;box-sizing:border-box}
html,body{width:1200px;height:1200px;overflow:hidden;background:var(--white)}
body{font-family:'Inter',sans-serif;color:var(--ink)}
.stage{position:absolute;left:0;top:0;width:1920px;height:1920px;transform:scale(.625);transform-origin:0 0}
.page{position:absolute;left:750px;top:61px;width:432px;height:1810px}
.page *{position:absolute}
.page span,.page b,.page i,.page br,.page em{position:static}
.btn{background:linear-gradient(90deg,var(--gold-light),var(--gold));color:var(--ink);font-size:3.6px;font-weight:600;display:flex;align-items:center;justify-content:center;white-space:nowrap}
.title{font-size:10.5px;font-weight:600;line-height:1.25;color:var(--ink);white-space:nowrap}
.title b{color:var(--gold);font-weight:600}
.small{font-size:3.8px;line-height:1.55;color:var(--muted)}

/* nav */
.nav{left:0;top:0;width:432px;height:31px;background:var(--black)}
.brand{left:28px;top:8px;display:flex;align-items:center;gap:5px;color:var(--gold);font-family:'Jost',sans-serif;font-size:10px;font-weight:500;letter-spacing:.3px}
.brand-dot{display:block;width:13px;height:13px;border-radius:50%;border:1.5px solid var(--gold)}
.nav-links{left:217px;top:13px;display:flex;gap:5px;font-size:4.4px;color:var(--gold);white-space:nowrap}

/* hero */
.hero{left:0;top:31px;width:432px;height:209px;background:linear-gradient(90deg,#45484d 0%,#5a5d62 45%,#7a7b7c 70%,#4d4f53 100%)}
.hero-title{left:27px;top:40px;font-family:'Jost',sans-serif;font-size:14.5px;font-weight:600;line-height:1.27;color:var(--gold);white-space:nowrap}
.hero-text{left:27px;top:103px;width:128px;font-size:4.3px;line-height:1.6;color:var(--white)}
.hero-btn{left:27px;top:150px;width:36px;height:11px}
.dots{display:flex;gap:4px}
.dots i{display:block;width:2px;height:2px;border-radius:50%;background:var(--white)}
.hero .dots{left:208px;top:183px}

/* benefits */
.why-title{left:0;top:255px;width:432px;text-align:center}
.benefit{width:100px;text-align:center}
.benefit .icon{position:relative;margin:0 auto;width:29px;height:29px;border-radius:50%;background:var(--slate-dark);border:2px solid var(--gold);display:block}
.benefit .icon::after{content:"";position:absolute;left:6px;top:6px;width:13px;height:13px;border-radius:50%;border:1.2px solid var(--gold)}
.benefit h3{position:static;margin-top:8px;font-size:5.8px;font-weight:500;white-space:nowrap}
.benefit p{position:static;margin-top:2px;font-size:3.8px;line-height:1.5;color:#333}
.vdiv{width:1px;height:48px;background:var(--line)}
.hdiv{left:27px;top:374px;width:378px;height:1px;background:#f3e4d0}

/* future */
.future{left:0;top:471px;width:432px;height:121px;background:var(--beige);overflow:hidden}
.future-photo{left:219px;top:0;width:240px;height:121px;border-radius:70px 0 0 70px;background:linear-gradient(90deg,#efcb4c,#e7c15a 55%,#dcb365)}
.future .title{left:27px;top:27px}
.future .small{left:27px;top:59px;width:136px;font-size:3.7px}

/* how to */
.howto-photo{left:86px;top:616px;width:127px;height:144px;background:linear-gradient(160deg,#f2f2f2,#dedede 60%,#cfe3ec)}
.howto .title{left:243px;top:628px}
.steps{left:243px;top:663px;width:170px}
.steps p{position:static;display:flex;align-items:center;gap:3px;font-size:3.8px;color:#444;margin-bottom:5px;white-space:nowrap}
.steps p i{width:4.5px;height:4.5px;background:var(--gold);display:block;flex:none}
.shop-btn{left:243px;top:720px;width:37px;height:10px}

/* products */
.products{left:0;top:785px;width:432px;height:223px;background:linear-gradient(180deg,var(--yellow),#f2d75a 60%,var(--yellow))}
.seal{left:197px;top:-14px;width:32px;height:32px;border-radius:50%;background:var(--white);display:flex;align-items:center;justify-content:center}
.seal i{display:block;width:14px;height:14px;border-radius:50%;border:1.5px solid var(--gold)}
.products .title{left:0;top:21px;width:432px;text-align:center}
.card{top:62px;width:89px;height:129px;background:var(--white)}
.bottle{left:28px;top:6px;width:33px;height:74px;border-radius:4px 4px 3px 3px}
.bottle.orange{background:linear-gradient(90deg,#f3a43a,#f7c36a,#f2a032)}
.bottle.blue{background:linear-gradient(90deg,#cfe4ee,#f2f1e4,#c6dfec)}
.card .name{left:0;top:92px;width:89px;text-align:center;font-size:5.6px;color:#333}
.card .price{left:30px;top:107px;width:30px;height:11px;font-size:4px}

/* reviews */
.reviews{left:0;top:1008px;width:432px;height:210px;background:var(--grey-bg)}
.reviews .title{left:0;top:25px;width:432px;text-align:center}
.review{top:72px;width:186px;height:102px;background:var(--cream);border-radius:3px;box-shadow:0 2px 6px rgba(0,0,0,.06)}
.review .quote{left:30px;top:26px;width:126px;text-align:center;font-size:3.8px;line-height:1.55;color:var(--muted)}
.avatar{left:86px;top:47px;width:16px;height:16px;border-radius:50%;background:#8a8f98}
.review .who{left:0;top:68px;width:186px;text-align:center;font-size:4px;font-weight:600}
.review .stars{left:0;top:75px;width:186px;text-align:center;font-size:3.5px;color:var(--gold);letter-spacing:.5px}
.reviews .dots{left:208px;top:194px}
.reviews .dots i{background:#bbb}
.reviews .dots i.on{background:#444}

/* faq */
.faq-photo{left:67px;top:1254px;width:144px;height:151px;border-radius:3px;background:linear-gradient(180deg,#f6c88f,#f3b46b 60%,#efa657)}
.faq-title{left:220px;top:1242px}
.faq-item{left:220px;width:163px;height:16px;background:var(--slate-dark);display:flex;align-items:center;gap:4px;padding:0 6px;font-size:3.7px;color:var(--white);font-weight:600;white-space:nowrap}
.faq-item b{color:var(--gold);font-weight:500}
.faq-item em{position:absolute !important;right:6px;font-style:normal;color:#aaa}
.faq-answer{left:220px;top:1291px;width:163px;height:40px;background:var(--white);border:1px solid #e4e4e4;border-top:0;padding:9px 8px;font-size:3.8px;line-height:1.6;color:var(--muted)}
.more-btn{left:170px;top:1436px;width:92px;height:11px}

/* contact */
.contact{left:0;top:1474px;width:432px;height:206px;background:var(--slate)}
.field{background:var(--white);font-size:3.8px;color:#888;padding:0 7px;display:flex;align-items:center}
.field.msg{align-items:flex-end;padding-bottom:9px}
.submit{left:194px;top:169px;width:43px;height:12px}

/* footer */
.footer{left:0;top:1680px;width:432px;height:115px;background:var(--black);color:var(--white)}
.footer .brand{left:27px;top:22px;flex-direction:column;align-items:flex-start;gap:3px;font-size:6.5px}
.footer .brand-dot{width:26px;height:26px;margin-left:8px}
.f-contact{left:27px;top:70px;font-size:3.8px;line-height:1.8;white-space:nowrap}
.f-col{top:20px;font-size:3.8px;line-height:2.6;white-space:nowrap}
.f-col h4{position:static;font-size:4px;font-weight:600;margin-bottom:1px}
.f-news{left:277px;top:20px;width:128px;font-size:3.8px;line-height:1.8;font-weight:500;white-space:nowrap}
.f-input{left:277px;top:37px;width:76px;height:18px;background:var(--white);color:#999;font-size:3.8px;padding:0 6px;display:flex;align-items:center}
.f-sub{left:353px;top:37px;width:52px;height:18px;font-size:3.8px}
.socials{left:277px;top:62px;display:flex;gap:7px}
.socials i{width:9px;height:9px;border-radius:50%;background:var(--gold);display:block}
.cards{left:277px;top:90px;display:flex;gap:2px}
.cards i{width:10px;height:6px;border-radius:1px;display:block;background:#4a6fd1}
.cards i:first-child{background:#e24b3a}
.cards i:nth-child(4){background:#d98b2d}
.bottom{left:0;top:1795px;width:432px;height:15px;font-size:3.6px;color:#333}
.bottom .copy{left:39px;top:5px;white-space:nowrap}
.bottom .links{left:255px;top:5px;display:flex;gap:7px;white-space:nowrap}
</style>
</head>
<body>
<div class="stage">
<main class="page">

  <header class="nav">
    <div class="brand"><span class="brand-dot"></span><span>PLOOIFRIS</span></div>
    <nav class="nav-links"><span>HOME</span><span>ABOUT US</span><span>PRODUCT</span><span>TESTIMONIAL</span><span>CONTACT</span></nav>
  </header>

  <section class="hero" role="img" aria-label="Photo of a person holding a soft white towel to their face">
    <h1 class="hero-title">Experience Luxury<br>And Sustainability<br>In Every Wash)</h1>
    <p class="hero-text">Discover the unparalleled quality of Plooifris's premium laundry strips – a perfect blend of luxury and eco-consciousness. Elevate your laundry experience with a product that redefines sophistication, care, and sustainability in every wash.</p>
    <div class="btn hero-btn">Try Now</div>
    <div class="dots"><i></i><i></i><i></i></div>
  </section>

  <h2 class="title why-title">Why Choose Plooifris<br>Laundry Strips?)</h2>
  <div class="benefit" style="left:53px;top:300px"><span class="icon"></span><h3>Eco - Friendly</h3><p>100% biodegradable and<br>plastic-free.</p></div>
  <div class="benefit" style="left:163px;top:300px"><span class="icon"></span><h3>Suitable for All Fabrics</h3><p>Safe for delicate laundry,<br>whites, colors, and blacks</p></div>
  <div class="benefit" style="left:275px;top:300px"><span class="icon"></span><h3>Suitable for All Fabrics</h3><p>No hassle with heavy bottles<br>– just tear, add, and enjoy.</p></div>
  <div class="vdiv" style="left:156px;top:305px"></div>
  <div class="vdiv" style="left:270px;top:305px"></div>
  <div class="hdiv"></div>
  <div class="benefit" style="left:55px;top:384px"><span class="icon"></span><h3>Long-Lasting Scent</h3><p>A delightful fresh scent that<br>lingers for days.</p></div>
  <div class="benefit" style="left:165px;top:384px"><span class="icon"></span><h3>Hypoallergenic</h3><p>Perfect for sensitive skin and<br>baby clothing.</p></div>
  <div class="benefit" style="left:277px;top:384px"><span class="icon"></span><h3>Always Free Shipping</h3><p>No minimum order quantity<br>required</p></div>
  <div class="vdiv" style="left:156px;top:389px"></div>
  <div class="vdiv" style="left:270px;top:389px"></div>

  <section class="future">
    <div class="future-photo" role="img" aria-label="Photo of a woman smelling freshly washed laundry, golden tint"></div>
    <h2 class="title">The <b>Future</b> Of<br>Laundry Is Here</h2>
    <p class="small">Our Plooifris Laundry Strips combine innovation with sustainability. With just one strip per load, enjoy clean and beautifully scented laundry without burdening the environment. No plastic bottles, no waste – just pure freshness.</p>
  </section>

  <section class="howto">
    <div class="howto-photo" role="img" aria-label="Photo of hands tearing a laundry strip from its pack"></div>
    <h2 class="title">How To Use<br><b>Laundry</b> Strips</h2>
    <div class="steps">
      <p><i></i>Tear off a laundry strip.</p>
      <p><i></i>Place the strip directly in the drum with your laundry.</p>
      <p><i></i>Start the washing machine and let the strip do its work.)</p>
      <p><i></i>Enjoy perfectly clean and fresh-smelling clothes!</p>
    </div>
    <div class="btn shop-btn">Shop Now</div>
  </section>

  <section class="products">
    <div class="seal"><i></i></div>
    <h2 class="title">New Product</h2>
    <div class="card" style="left:27px"><div class="bottle orange" role="img" aria-label="Orange patterned detergent bottle"></div><p class="name">Name Product</p><div class="btn price">$14.95</div></div>
    <div class="card" style="left:123px"><div class="bottle blue" role="img" aria-label="Blue patterned detergent bottle"></div><p class="name">Name Product</p><div class="btn price">$14.95</div></div>
    <div class="card" style="left:220px"><div class="bottle orange" role="img" aria-label="Orange patterned detergent bottle"></div><p class="name">Name Product</p><div class="btn price">$14.95</div></div>
    <div class="card" style="left:316px"><div class="bottle blue" role="img" aria-label="Blue patterned detergent bottle"></div><p class="name">Name Product</p><div class="btn price">$14.95</div></div>
  </section>

  <section class="reviews">
    <h2 class="title">What Our<br><b>Customers</b> Say</h2>
    <article class="review" style="left:27px">
      <p class="quote">❝ Since using Plooifris, my laundry feels fresher and more luxurious than ever</p>
      <div class="avatar" role="img" aria-label="Customer portrait"></div>
      <p class="who">Lotte</p><p class="stars">★★★★★</p>
    </article>
    <article class="review" style="left:220px">
      <p class="quote">❝ Finally, an eco-friendly product that truly works and smells wonderful</p>
      <div class="avatar" role="img" aria-label="Customer portrait"></div>
      <p class="who">Daan</p><p class="stars">★★★★★</p>
    </article>
    <div class="dots"><i></i><i class="on"></i><i></i></div>
  </section>

  <section class="faq">
    <div class="faq-photo" role="img" aria-label="Photo of two hands holding laundry strips on an orange backdrop"></div>
    <h2 class="title faq-title">Do You Have Any<br><b>Questions ?</b></h2>
    <div class="faq-item" style="top:1275px"><b>01</b>Are the strips suitable for people with sensitive skin?<em>–</em></div>
    <p class="faq-answer">Yes, our strips are hypoallergenic and dermatologically tested, making them safe for sensitive skin.</p>
    <div class="faq-item" style="top:1339px"><b>02</b>How many washes does one pack contain?<em>+</em></div>
    <div class="faq-item" style="top:1363px"><b>03</b>Do the strips work at low temperatures?<em>+</em></div>
    <div class="faq-item" style="top:1387px"><b>04</b>How can set notification?<em>+</em></div>
    <div class="btn more-btn">Check Our FAQ for More Answers</div>
  </section>

  <section class="contact">
    <div class="field" style="left:67px;top:56px;width:153px;height:18px">FIRST NAME</div>
    <div class="field" style="left:227px;top:56px;width:153px;height:18px">LAST NAME</div>
    <div class="field" style="left:67px;top:84px;width:153px;height:19px">EMAIL</div>
    <div class="field" style="left:227px;top:84px;width:153px;height:19px">PHONE</div>
    <div class="field msg" style="left:67px;top:113px;width:313px;height:45px">MESSAGE</div>
    <div class="btn submit">SUBMIT</div>
  </section>

  <footer class="footer">
    <div class="brand"><span class="brand-dot"></span><span>PLOOIFRIS</span></div>
    <p class="f-contact">Email: support@plooifris.nl<br>Phone: +31 20 555 0148<br>Address</p>
    <div class="f-col" style="left:112px"><h4>Quick Link</h4>About Us<br>Contact Us<br>FAQ<br>Shipping &amp; Returns<br>Privacy Policy</div>
    <div class="f-col" style="left:192px"><h4>Quick Link</h4>About Us<br>Contact Us<br>FAQ<br>Shipping &amp; Returns<br>Privacy Policy</div>
    <p class="f-news">Start Today with Eco-Friendly Laundry!<br>No Plastic, No Hassle. Just Fresh Laundry</p>
    <div class="f-input">Enter Email Address</div>
    <div class="btn f-sub">SUBSCRIBE</div>
    <div class="socials"><i></i><i></i><i></i><i></i></div>
    <div class="cards"><i></i><i></i><i></i><i></i><i></i></div>
  </footer>

  <div class="bottom">
    <p class="copy">Copyright © 2024 www.plooifris.nl All Rights Reserved</p>
    <p class="links"><span>Home</span><span>Why Us</span><span>Testimonials</span><span>Pricing</span><span>FAQ</span><span>Contact Us</span></p>
  </div>

</main>
</div>
</body>
</html>
```